Design a sharp Business Card, Stationary, and PowerPoint Template for Harbor Lantern Group (HLG)
Harbor Lantern Group (HLG) is a consulting firm with a mission
Professional
Maren Coleby Ashdown
Managing Director
4870 Larkspur Blvd. NW
Suite 2300
Washington, DC 20417
maren@harborlntn.example
www.harborlntn.example
I'm looking for something sharp that incorporates the colors of the logo.
Business card designs (only), please include this text:
We work with the military, private sector, and nonprofits to protect people affected by conflict and disaster.
This is the logo for Harbor Lantern Group (HLG). The black and red color combo is preferred.
For design purposes, the symbol can be used separately from the text and watermarked.

```html
<!DOCTYPE html>
<html lang="en">
<head>
<meta charset="utf-8">
<title>Harbor Lantern Group — Business Card</title>
<link rel="stylesheet" href="https://fonts.googleapis.com/css2?family=Open+Sans:wght@300;400;600;700&display=swap">
<style>
  :root {
    --stage: #e9eaec;
    --card-dark: #2f2f31;
    --card-light: #ffffff;
    --brand-red: #d4202c;
    --ink: #3b3b3d;
    --ink-soft: #6d6d70;
    --line-grey: #c9c9cc;
    --on-dark: #ffffff;
  }
  * { box-sizing: border-box; margin: 0; padding: 0; }
  html, body {
    width: 1200px; height: 1009px; overflow: hidden;
    background: var(--stage);
    font-family: "Open Sans", Arial, sans-serif;
  }
  .stage { position: relative; width: 1200px; height: 1009px; }

  .card {
    position: absolute;
    width: 620px; height: 354px;
    border-radius: 22px;
    overflow: hidden;
    box-shadow: 0 10px 30px rgba(0,0,0,.18);
  }

  /* Back of card */
  .card-back {
    left: 500px; top: 110px;
    background: var(--card-dark);
    color: var(--on-dark);
    text-align: center;
  }
  .card-back .brand {
    position: absolute; left: 0; right: 0; top: 96px;
    display: flex; align-items: center; justify-content: center; gap: 14px;
  }
  .brand-dot {
    width: 46px; height: 46px; border-radius: 50%;
    background: var(--brand-red);
  }
  .card-back .brand-name {
    font-weight: 300; font-size: 26px; letter-spacing: 3px;
    text-transform: uppercase; color: var(--on-dark);
  }
  .mission {
    position: absolute; left: 60px; right: 60px; top: 190px;
    font-size: 13px; line-height: 1.45; font-weight: 400;
  }
  .mission .sectors {
    display: block; font-weight: 700; letter-spacing: .5px;
    text-transform: uppercase;
  }

  /* Front of card */
  .card-front {
    left: 80px; top: 540px;
    background: var(--card-light);
  }
  .card-front .swoosh { position: absolute; inset: 0; }
  .card-front .brand {
    position: absolute; left: 220px; top: 30px;
    display: flex; align-items: center; gap: 14px;
  }
  .card-front .brand-name {
    font-weight: 300; font-size: 20px; line-height: 1.25;
    letter-spacing: 4px; text-transform: uppercase; color: var(--ink);
  }
  .person {
    position: absolute; left: 44px; top: 136px;
    font-size: 12px; line-height: 1.5; color: var(--ink-soft);
  }
  .person .name {
    color: var(--brand-red); font-size: 15px; font-weight: 600;
  }
  .person .role { font-style: italic; margin-bottom: 2px; }

  .contacts {
    position: absolute; left: 356px; top: 138px;
    list-style: none; font-size: 12px; line-height: 1; color: var(--ink-soft);
  }
  .contacts li { display: flex; align-items: center; gap: 9px; margin-bottom: 7px; }
  .contacts .icon {
    width: 16px; height: 16px; border-radius: 50%;
    background: var(--brand-red); flex: none;
    display: flex; align-items: center; justify-content: center;
  }
  .contacts .icon svg { width: 10px; height: 10px; }
</style>
</head>
<body>
<main class="stage">

  <section class="card card-back" aria-label="Business card, back">
    <div class="brand">
      <span class="brand-dot"></span>
      <span class="brand-name">Harbor Lantern Group</span>
    </div>
    <p class="mission">
      We work with the
      <span class="sectors">Military | Private Sector | Nonprofits</span>
      to protect people affected by conflict and disaster.
    </p>
  </section>

  <section class="card card-front" aria-label="Business card, front">
    <svg class="swoosh" viewBox="0 0 620 354" preserveAspectRatio="none" aria-hidden="true">
      <path d="M0 282 C170 336 330 258 620 292 L620 354 L0 354 Z" fill="var(--card-dark)"/>
      <path d="M0 250 C160 302 330 226 620 260 L620 276 C330 244 170 320 0 268 Z" fill="var(--brand-red)"/>
      <path d="M0 270 C165 324 330 248 620 282" fill="none" stroke="var(--line-grey)" stroke-width="2"/>
      <path d="M0 238 C160 290 330 216 620 250" fill="none" stroke="var(--brand-red)" stroke-width="1.2"/>
    </svg>

    <div class="brand">
      <span class="brand-dot"></span>
      <span class="brand-name">Harbor<br>Lantern<br>Group</span>
    </div>

    <div class="person">
      <p class="name">Maren Coleby Ashdown</p>
      <p class="role">Managing Director</p>
      <p>4870 Larkspur Blvd. NW</p>
      <p>Suite 2300 Washington, DC 20417</p>
    </div>

    <ul class="contacts">
      <li><span class="icon"><svg viewBox="0 0 10 10"><path d="M2 1 L4 1 L4.6 3 L3.5 3.8 C4 5 5 6 6.2 6.5 L7 5.4 L9 6 L9 8 C5 8.5 1.5 5 2 1 Z" fill="#fff"/></svg></span>202-555-0147</li>
      <li><span class="icon"><svg viewBox="0 0 10 10"><rect x="3" y="1" width="4" height="8" rx="1" fill="#fff"/></svg></span>202-555-0183</li>
      <li><span class="icon"><svg viewBox="0 0 10 10"><rect x="1" y="2.5" width="8" height="5.5" fill="#fff"/><path d="M1 2.5 L5 5.8 L9 2.5" stroke="#d4202c" stroke-width=".8" fill="none"/></svg></span>maren@harborlntn.example</li>
      <li><span class="icon"><svg viewBox="0 0 10 10"><circle cx="5" cy="5" r="3.6" fill="none" stroke="#fff" stroke-width="1"/><path d="M1.4 5 H8.6 M5 1.4 C3 3.5 3 6.5 5 8.6 M5 1.4 C7 3.5 7 6.5 5 8.6" stroke="#fff" stroke-width=".8" fill="none"/></svg></span>www.harborlntn.example</li>
    </ul>
  </section>

</main>
</body>
</html>
```